New Business Card Design Project

We beed a business card design that doesn't look too cluttered that contains:
- our logo
- our email
- our phone number
- our website
- dosing chart
- statement that says "Exclusive Distributor for Vantrolix(R) (Qld, NSW, Vic)"

It is for a health product safe for mums, bubs, pregnant and breastfeeding women - icons for these would be great for the card if they will not overwhelm the card.

It is a toxin and pathogen binder in the gut so it sucks out bad viruses, bacteria and funguses, but leaves the beneficial flora where it should be to flourish.

Thank you for taking on this project. I look forward to seeing your work.

Target Market(s)

Parents, anyone with gut dysfunction

Industry/Entity Type

Health Product

Contact Information for Business Card

Phone - 1300 571 946
email - orders@duvameKA.com.au
website - duvameKA.com.au
Exclusive Distributors for Vantrolix(R) (Qld, NSW, Vic) - note (R) is for Registered TM Logo so it should be an R in a circle

Font styles to use
Sans Serif

Requirements
Must have
• our logo - please see DKA Logo Options for both logo on white and logo on black options.
• our email
• our phone number enlarged
• our website
• our dosing chart (chart only) information underneath it on the image is not required
• our statement - Exclusive Distributor for Vantrolix(R) (Qld, NSW, Vic)
Nice to have
• - curved corners on the business cards
• - photo of a tube of the product if it can fit
• - the little people icons as in the product flyer indicating it is safe for children, babies, pregnancy, breastfeeding etc.
Should not have
• clutter!
• Must be easy to read.
• I would prefer to see less on the card with more punch so please omit our photo of the product if necessary.

```html
<!DOCTYPE html>
<html lang="en">
<head>
<meta charset="utf-8">
<title>duvameKA business card</title>
<link rel="stylesheet" href="https://fonts.googleapis.com/css2?family=Questrial&display=swap">
<style>
  :root {
    --backdrop: #2b2b2d;
    --card: #0d0d0e;
    --card-edge: #1c1c1e;
    --brand-blue: #1e8fe0;
    --text-light: #d9dde2;
    --text-muted: #9aa3ad;
    --icon-blue: #5aa8e6;
    --rule: #2a3a4a;
  }
  * { margin: 0; padding: 0; box-sizing: border-box; }
  html, body {
    width: 1200px;
    height: 900px;
    overflow: hidden;
    background: var(--backdrop);
    font-family: "Questrial", sans-serif;
  }
  .card-set {
    position: relative;
    width: 1200px;
    height: 900px;
  }
  .card {
    position: absolute;
    top: 292px;
    width: 520px;
    height: 316px;
    border-radius: 26px;
    background: var(--card);
    border: 1px solid var(--card-edge);
    overflow: hidden;
  }
  .card--contact { left: 60px; }
  .card--brand { left: 620px; }

  /* contact side */
  .brand-mark {
    position: absolute;
    left: 36px;
    top: 124px;
    display: flex;
    align-items: center;
    gap: 10px;
    color: var(--brand-blue);
    font-size: 26px;
    white-space: nowrap;
  }
  .brand-mark__dot {
    width: 16px;
    height: 16px;
    border-radius: 50%;
    background: var(--brand-blue);
  }
  .divider {
    position: absolute;
    left: 238px;
    top: 50px;
    width: 2px;
    height: 180px;
    background: linear-gradient(to bottom, transparent, var(--brand-blue) 45%, transparent);
  }
  .contact-list {
    position: absolute;
    left: 262px;
    top: 92px;
    list-style: none;
    color: var(--text-light);
    font-size: 14px;
    line-height: 1;
  }
  .contact-list li {
    display: flex;
    align-items: center;
    gap: 10px;
    margin-bottom: 14px;
    white-space: nowrap;
  }
  .contact-list .contact-list__phone {
    font-size: 22px;
    color: #ffffff;
    margin-bottom: 18px;
  }
  .contact-list svg { width: 13px; height: 13px; flex: none; }
  .contact-list__phone svg { width: 16px; height: 16px; }
  .distributor-note {
    position: absolute;
    left: 0;
    right: 0;
    bottom: 30px;
    text-align: center;
    color: var(--text-muted);
    font-size: 12px;
    letter-spacing: 0.3px;
  }

  /* brand side */
  .brand-name {
    position: absolute;
    left: 0;
    right: 0;
    top: 52px;
    text-align: center;
    color: var(--brand-blue);
    font-size: 40px;
  }
  .dosing-chart {
    position: absolute;
    left: 110px;
    top: 140px;
    width: 300px;
    border-collapse: collapse;
    color: var(--text-light);
    font-size: 13px;
  }
  .dosing-chart caption {
    color: var(--brand-blue);
    font-size: 13px;
    letter-spacing: 1px;
    text-transform: uppercase;
    padding-bottom: 8px;
  }
  .dosing-chart th,
  .dosing-chart td {
    padding: 6px 10px;
    border-bottom: 1px solid var(--rule);
    text-align: left;
  }
  .dosing-chart th {
    color: var(--text-muted);
    font-weight: normal;
    font-size: 12px;
  }
  .dosing-chart td:last-child,
  .dosing-chart th:last-child { text-align: right; }
</style>
</head>
<body>
<main class="card-set">
  <section class="card card--contact">
    <div class="brand-mark">
      <span class="brand-mark__dot"></span>
      <span>duvameKA</span>
    </div>
    <div class="divider"></div>
    <ul class="contact-list">
      <li class="contact-list__phone">
        <svg viewBox="0 0 16 16" aria-hidden="true"><path fill="var(--icon-blue)" d="M3.5 1.5l2.5 0 1 3.5-1.8 1.3a9 9 0 0 0 4.5 4.5L11 9l3.5 1v2.5c0 1-1 2-2 2C6.5 14.5 1.5 9.5 1.5 3.5c0-1 1-2 2-2z"/></svg>
        <span>1300 571 946</span>
      </li>
      <li>
        <svg viewBox="0 0 16 16" aria-hidden="true"><rect x="1.5" y="3.5" width="13" height="9" rx="1" fill="none" stroke="var(--icon-blue)" stroke-width="1.6"/><path d="M2 4l6 5 6-5" fill="none" stroke="var(--icon-blue)" stroke-width="1.6"/></svg>
        <span>orders@duvameKA.com.au</span>
      </li>
      <li>
        <svg viewBox="0 0 16 16" aria-hidden="true"><circle cx="8" cy="8" r="6.5" fill="none" stroke="var(--icon-blue)" stroke-width="1.5"/><ellipse cx="8" cy="8" rx="2.8" ry="6.5" fill="none" stroke="var(--icon-blue)" stroke-width="1.2"/><path d="M1.5 8h13" stroke="var(--icon-blue)" stroke-width="1.2"/></svg>
        <span>duvameKA.com.au</span>
      </li>
    </ul>
    <p class="distributor-note">Exclusive Distributor for Vantrolix® (Qld, NSW, Vic)</p>
  </section>

  <section class="card card--brand">
    <div class="brand-name">duvameKA</div>
    <table class="dosing-chart">
      <caption>Dosing chart</caption>
      <thead>
        <tr><th>Age</th><th>Daily dose</th></tr>
      </thead>
      <tbody>
        <tr><td>Babies</td><td>x g</td></tr>
        <tr><td>Children</td><td>x g</td></tr>
        <tr><td>Adults</td><td>x g</td></tr>
      </tbody>
    </table>
  </section>
</main>
</body>
</html>
```